5 website banners (slides show)

We need 5 website sliding banners created for a website all about internet safety. The topics for each banner are:

Cyberbullying
Fraud
seniors
social networking

Sizes: 953 pixels x 281 pixels

I have stock images to use or feel free to use your own or one I can purchase from pixelvarro.example.

Industry/Entity Type

Internet

```html
<!DOCTYPE html>
<html lang="en">
<head>
<meta charset="utf-8">
<title>Talk About The Digital World – Seniors</title>
<link rel="stylesheet" href="https://fonts.googleapis.com/css2?family=PT+Sans:wght@400;700&display=swap">
<style>
  :root {
    --magenta: #e5097f;
    --magenta-deep: #d4006f;
    --leaf: #7fc241;
    --leaf-dark: #3f8a3a;
    --leaf-light: #9ed45a;
    --ink: #1a1a1a;
    --white: #ffffff;
    --photo-sky: #cfe3ec;
    --photo-warm: #c89a7c;
    --photo-shade: #5a3a2c;
    --photo-light: #efe6dc;
  }
  html, body {
    margin: 0;
    padding: 0;
    width: 1200px;
    height: 354px;
    overflow: hidden;
    background: var(--white);
  }
  .banner {
    position: relative;
    width: 1200px;
    height: 354px;
    background: var(--magenta);
    border-radius: 10px;
    overflow: hidden;
    font-family: "PT Sans", Arial, sans-serif;
  }
  .banner__frame {
    position: absolute;
    inset: 7px;
    border: 2px dotted rgba(255,255,255,0.85);
    border-radius: 8px;
    pointer-events: none;
    z-index: 4;
  }
  .banner__photo {
    position: absolute;
    left: 13px;
    top: 13px;
    width: 610px;
    height: 328px;
    background:
      radial-gradient(ellipse at 55% 45%, var(--photo-warm) 0%, rgba(200,154,124,0) 45%),
      radial-gradient(ellipse at 20% 70%, var(--photo-shade) 0%, rgba(90,58,44,0) 40%),
      linear-gradient(180deg, var(--photo-sky) 0%, var(--photo-light) 60%, var(--photo-warm) 100%);
    -webkit-mask-image: linear-gradient(90deg, #000 0%, #000 80%, transparent 100%);
    mask-image: linear-gradient(90deg, #000 0%, #000 80%, transparent 100%);
    z-index: 1;
  }
  .banner__headline {
    position: absolute;
    left: 657px;
    top: 112px;
    margin: 0;
    font-size: 66px;
    font-weight: 700;
    line-height: 76px;
    color: var(--leaf);
    text-shadow: 2px 3px 4px rgba(60,0,30,0.55);
    letter-spacing: 0.3px;
    z-index: 2;
  }
  .topic-tag {
    position: absolute;
    left: 44px;
    top: 239px;
    z-index: 3;
  }
  .topic-tag svg { display: block; }
  .topic-tag__label {
    position: absolute;
    left: 0;
    top: 0;
    width: 180px;
    height: 48px;
    line-height: 48px;
    text-align: center;
    font-size: 29px;
    font-weight: 400;
    color: var(--ink);
  }
  .slide-dots {
    position: absolute;
    left: 1077px;
    top: 301px;
    display: flex;
    gap: 9px;
    z-index: 3;
  }
  .slide-dots__item {
    width: 19px;
    height: 19px;
    border: 3px solid var(--white);
    border-radius: 2px;
  }
  .slide-dots__item--one { background: var(--leaf-dark); }
  .slide-dots__item--two { background: var(--leaf); }
  .slide-dots__item--three { background: var(--leaf-light); }
</style>
</head>
<body>
  <div class="banner">
    <div class="banner__photo" role="img" aria-label="Photo of a smiling family with two young children looking at a laptop together"></div>

    <h1 class="banner__headline">Talk About The<br>Degital World</h1>

    <div class="topic-tag">
      <svg width="184" height="62" viewBox="0 0 184 62" aria-hidden="true">
        <path d="M8 1 H172 Q180 1 180 9 V40 Q180 48 172 48 H158 L150 60 L146 48 H8 Q1 48 1 40 V9 Q1 1 8 1 Z"
              fill="var(--leaf)" stroke="#2b3a1c" stroke-width="2"/>
      </svg>
      <span class="topic-tag__label">Seniors</span>
    </div>

    <div class="slide-dots" aria-hidden="true">
      <span class="slide-dots__item slide-dots__item--one"></span>
      <span class="slide-dots__item slide-dots__item--two"></span>
      <span class="slide-dots__item slide-dots__item--three"></span>
    </div>

    <div class="banner__frame"></div>
  </div>
</body>
</html>
```